Spring Savings Package for The Lodge at Harlan's Meadow Lodge

Design an email and elevator poster 11x7 that promotes Spring and our heated pools at The Lodge at Harlan's Meadow
Text-

Worried about the Spring Weather don't #IndoorWaterpark !

Ask about our Springtime Savings that comes with a Free Resort Beach Towel ($12 value).

Book by March 1st,2019
Stay Dates Now-May 23rd,2019

Phone number: 800.555.0192

Reserve Now! www (dot) lodgeatharlansmeadow (dot) com

Target Market(s)

Guest reserving Spring Break

Industry/Entity Type

Hospitality

Requirements
Must have
• text
• phone
• website
• Book Now
• Can change some of the text to make it more of a Sales piece
Nice to have
• Brand Colors

```html
<!DOCTYPE html>
<html lang="en">
<head>
<meta charset="utf-8">
<title>The Lodge at Harlan's Meadow – Promo Material</title>
<link href="https://fonts.googleapis.com/css2?family=Fredoka:wght@500;600&family=Source+Sans+3:wght@400;600&display=swap" rel="stylesheet">
<style>
:root{
  --board:#f1f1f1;
  --teal:#4f7a8b;
  --tan:#e0a75e;
  --gold:#d99a4b;
  --ink:#4a3c2e;
  --cream:#fcf6e9;
  --white:#ffffff;
}
*{margin:0;padding:0;box-sizing:border-box}
html,body{width:1200px;height:1189px;overflow:hidden;background:var(--board)}
body{position:relative;font-family:"Source Sans 3",Arial,sans-serif;color:var(--ink)}
.board-title{position:absolute;left:50px;top:88px;font-size:18px;color:var(--teal);letter-spacing:.2px}
.board-title strong{font-weight:600}
.board-title span{font-weight:400;color:#7f9aa5}
.board-rule{position:absolute;left:50px;top:127px;width:1078px;height:1px;background:var(--teal)}
.piece-label{position:absolute;top:202px;font-size:14px;color:#555;letter-spacing:.3px}
.abs{position:absolute}
.display{font-family:"Fredoka",Arial,sans-serif;font-weight:600}

/* Email */
.email{position:absolute;left:52px;top:241px;width:454px;height:617px;background:var(--white);box-shadow:0 2px 6px rgba(0,0,0,.15);overflow:hidden}
.email svg.art{position:absolute;left:0;top:0}
.wordmark{font-family:"Fredoka",Arial,sans-serif;font-weight:600;color:var(--teal);text-align:center;line-height:1.05}
.email .wordmark{left:18px;top:48px;width:140px;font-size:17px}
.email .kicker{left:25px;top:178px;font-size:17px;color:var(--gold)}
.email .headline{left:25px;top:200px;font-size:24px;color:var(--teal);letter-spacing:.3px}
.email .offer{left:0;top:254px;width:260px;text-align:center;font-size:15px;line-height:19px}
.offer .hi{color:var(--gold);font-weight:600}
.email .divider{left:68px;top:365px;width:96px;height:1px;background:#b9a48a}
.email .dates{left:25px;top:381px;font-size:15px;line-height:24px}
.dates b{color:var(--teal);font-weight:600}
.email .book-btn{left:53px;top:453px;width:151px;height:33px;background:var(--teal);color:var(--white);font-weight:600;font-size:15px;display:flex;align-items:center;justify-content:center}
.partner{font-family:"Fredoka",Arial,sans-serif;font-weight:600}
.email .partner-a{left:42px;top:525px;font-size:15px;color:#2a9fd6}
.email .partner-b{left:152px;top:525px;font-size:15px;color:var(--ink)}
.email .footer{left:0;top:583px;width:454px;height:34px;background:var(--tan);border-top:3px solid var(--teal);color:var(--white);font-weight:600;font-size:13px}
.footer .ph{position:absolute;left:28px;top:7px;display:flex;align-items:center;gap:4px}
.footer .web{position:absolute;left:164px;top:7px;display:flex;align-items:center;gap:8px}

/* Poster */
.poster{position:absolute;left:572px;top:241px;width:558px;height:877px;background:var(--cream);box-shadow:0 2px 6px rgba(0,0,0,.15);overflow:hidden}
.poster svg.art{position:absolute;left:0;top:0}
.poster .wordmark{left:34px;top:70px;width:165px;font-size:22px}
.poster .partner-a{left:32px;top:180px;font-size:17px;color:var(--teal)}
.poster .partner-b{left:146px;top:180px;font-size:17px;color:var(--teal)}
.poster .kicker{left:22px;top:239px;font-size:21px;color:var(--teal)}
.kicker .hi{color:var(--gold)}
.poster .headline{left:24px;top:274px;font-size:30px;line-height:37px;color:var(--teal);letter-spacing:.3px}
.headline .hi{color:var(--gold)}
.poster .headline .big{font-size:35px}
.poster .offer{left:25px;top:370px;font-size:17px;line-height:20px;font-weight:600}
.poster .offer .soft{color:var(--gold);font-weight:400}
.poster .when{top:437px;font-size:17px;line-height:24px}
.when b{display:block;font-family:"Fredoka",Arial,sans-serif;font-weight:600;font-size:22px;color:var(--teal)}
.poster .reserve{left:382px;top:425px;width:172px;text-align:center;color:var(--tan);line-height:1}
.reserve .r1{font-size:29px;display:block}
.reserve .r2{font-size:42px;display:block;margin-top:4px}
.poster .contact{left:34px;font-size:18px;font-weight:600;color:var(--teal);display:flex;align-items:center;gap:9px}
</style>
</head>
<body>

<div class="board-title"><strong>THE LODGE AT HARLAN'S MEADOW</strong> <span>PROMO MATERIAL</span></div>
<div class="board-rule"></div>
<div class="piece-label" style="left:53px">E-MAIL</div>
<div class="piece-label" style="left:572px">POSTER</div>

<!-- Email -->
<section class="email">
  <svg class="art" width="454" height="617" viewBox="0 0 454 617">
    <defs>
      <linearGradient id="email-hero" x1="0" y1="0" x2="1" y2="1">
        <stop offset="0" stop-color="#e6b77a"/><stop offset=".55" stop-color="#b98f6a"/><stop offset="1" stop-color="#6f8fb8"/>
      </linearGradient>
      <linearGradient id="email-pool" x1="0" y1="0" x2="0" y2="1">
        <stop offset="0" stop-color="#c9d6dc"/><stop offset="1" stop-color="#6fa3bd"/>
      </linearGradient>
      <radialGradient id="email-slide" cx=".5" cy=".5" r=".6">
        <stop offset="0" stop-color="#6b4a2a"/><stop offset=".45" stop-color="#b9a33a"/><stop offset="1" stop-color="#e0d06a"/>
      </radialGradient>
    </defs>
    <rect x="0" y="0" width="454" height="160" fill="var(--tan)"/>
    <rect x="150" y="0" width="304" height="160" fill="url(#email-hero)" role="img" aria-label="Photo: kids on an inflatable float in front of the lodge and its outdoor slides"/>
    <path d="M0 110 L0 160 L150 160 C90 160 40 140 0 110Z" fill="var(--teal)"/>
    <circle cx="88" cy="58" r="106" fill="var(--tan)"/>
    <circle cx="84" cy="56" r="102" fill="var(--white)"/>
    <path d="M454 230 C380 250 318 290 312 360 L312 400 C340 390 400 385 454 380Z" fill="url(#email-pool)" role="img" aria-label="Photo: girls playing in the indoor splash pool"/>
    <path d="M454 226 C378 246 314 288 308 360" fill="none" stroke="var(--teal)" stroke-width="6"/>
    <path d="M454 233 C382 252 322 292 316 360" fill="none" stroke="var(--tan)" stroke-width="3"/>
    <circle cx="356" cy="471" r="92" fill="var(--tan)"/>
    <circle cx="356" cy="471" r="86" fill="url(#email-slide)" role="img" aria-label="Photo: girl cheering at the end of a yellow tube slide"/>
  </svg>
  <div class="abs wordmark">The Lodge at<br>Harlan's Meadow</div>
  <div class="abs display kicker">Worried about the spring weather? Don't be!</div>
  <div class="abs display headline">COME TO OUR INDOOR WATERPARK!</div>
  <div class="abs offer">Ask about our<br><span class="hi">SPRINGTIME SAVINGS</span><br>that comes with a<br><span class="hi">FREE RESORT BEACH TOWEL</span><br>($12 value)</div>
  <div class="abs divider"></div>
  <div class="abs dates"><b>BOOK BY:</b> March 1st, 2019<br><b>STAY DATES:</b> Now-May23rd, 2019</div>
  <div class="abs book-btn">BOOK NOW!</div>
  <div class="abs partner partner-a">Splash Hollow</div>
  <div class="abs partner partner-b">Lantern Bay</div>
  <div class="abs footer">
    <div class="ph"><svg width="13" height="13" viewBox="0 0 24 24"><circle cx="12" cy="12" r="12" fill="#fff"/><path d="M8 6c1 0 2 2 2 3s-1 1-1 2 2 3 3 3 1-1 2-1 3 1 3 2-1 2-2 2c-4 0-9-5-9-9 0-1 1-2 2-2z" fill="var(--tan)"/></svg>800.555.0192</div>
    <div class="web"><svg width="13" height="13" viewBox="0 0 24 24"><circle cx="12" cy="12" r="11" fill="none" stroke="#fff" stroke-width="2"/><rect x="6" y="8" width="12" height="8" fill="none" stroke="#fff" stroke-width="1.6"/><path d="M6 8l6 5 6-5" fill="none" stroke="#fff" stroke-width="1.6"/></svg>www.lodgeatharlansmeadow.com</div>
  </div>
</section>

<!-- Poster -->
<section class="poster">
  <svg class="art" width="558" height="877" viewBox="0 0 558 877">
    <defs>
      <linearGradient id="poster-slide" x1="0" y1="0" x2="1" y2="1">
        <stop offset="0" stop-color="#d9d2c4"/><stop offset=".45" stop-color="#cdbb55"/><stop offset=".75" stop-color="#8a6a3a"/><stop offset="1" stop-color="#e9ecee"/>
      </linearGradient>
      <linearGradient id="poster-float" x1="0" y1="0" x2="0" y2="1">
        <stop offset="0" stop-color="#c99a6a"/><stop offset=".5" stop-color="#8a6fb0"/><stop offset="1" stop-color="#7cc3e0"/>
      </linearGradient>
      <linearGradient id="poster-splash" x1="0" y1="0" x2="1" y2="1">
        <stop offset="0" stop-color="#b7c3c6"/><stop offset=".6" stop-color="#d9a7a0"/><stop offset="1" stop-color="#8c8a84"/>
      </linearGradient>
    </defs>
    <path d="M255 0 L558 0 L558 352 C500 345 430 350 375 358 C395 300 412 245 428 192 C380 210 320 222 272 216 C254 150 248 80 255 0Z" fill="url(#poster-slide)" role="img" aria-label="Photo: girl in a yellow tube slide splashing down, friend sitting nearby"/>
    <path d="M246 0 C239 80 246 150 265 218" fill="none" stroke="var(--teal)" stroke-width="8"/>
    <path d="M370 362 C384 374 398 384 412 394" fill="none" stroke="var(--teal)" stroke-width="6"/>
    <circle cx="474" cy="463" r="100" fill="var(--tan)"/>
    <circle cx="478" cy="465" r="91" fill="var(--teal)"/>
    <path d="M400 660 C440 610 500 585 558 578 L558 877 L400 877Z" fill="url(#poster-splash)" role="img" aria-label="Photo: girls splashing in the indoor pool"/>
    <path d="M0 590 C150 560 300 590 400 660 C430 720 450 800 400 877 L0 877Z" fill="url(#poster-float)" role="img" aria-label="Photo: kids on an inflatable float in front of the lodge"/>
    <path d="M0 586 C150 556 300 586 400 656 C430 716 452 800 402 877" fill="none" stroke="var(--tan)" stroke-width="8"/>
    <path d="M404 652 C444 604 500 580 558 574" fill="none" stroke="var(--teal)" stroke-width="9"/>
  </svg>
  <div class="abs wordmark">The Lodge at<br>Harlan's Meadow</div>
  <div class="abs partner partner-a">Splash Hollow</div>
  <div class="abs partner partner-b">Lantern Bay</div>
  <div class="abs display kicker">Worried <span class="hi">about the spring weather?</span></div>
  <div class="abs display headline"><span class="hi">DON'T BE!</span> COME TO OUR<br><span class="big">INDOORWATERPARK!</span></div>
  <div class="abs offer">Ask about our <span class="soft">Springtime Savings</span> that comes<br>with a <span style="color:var(--gold)">FREE RESORT BEACH TOWEL</span> ($12 value)</div>
  <div class="abs when" style="left:40px"><b>BOOK BY:</b>March 1st, 2019</div>
  <div class="abs when" style="left:185px"><b>STAY DATES:</b>Now-May23rd, 2019</div>
  <div class="abs display reserve"><span class="r1">RESERVE</span><span class="r2">NOW!</span></div>
  <div class="abs contact" style="top:511px"><svg width="18" height="18" viewBox="0 0 24 24"><circle cx="12" cy="12" r="12" fill="var(--teal)"/><path d="M8 6c1 0 2 2 2 3s-1 1-1 2 2 3 3 3 1-1 2-1 3 1 3 2-1 2-2 2c-4 0-9-5-9-9 0-1 1-2 2-2z" fill="var(--cream)"/></svg>800.555.0192</div>
  <div class="abs contact" style="top:537px"><svg width="18" height="18" viewBox="0 0 24 24"><circle cx="12" cy="12" r="12" fill="var(--teal)"/><rect x="6" y="8" width="12" height="8" fill="none" stroke="var(--cream)" stroke-width="1.6"/><path d="M6 8l6 5 6-5" fill="none" stroke="var(--cream)" stroke-width="1.6"/></svg>www.lodgeatharlansmeadow.com</div>
</section>

</body>
</html>
```